Lend a Lantern Website Design (design layout only)

We need a website design for a new nonprofit organization based in Des Moines, Iowa called Lend a Lantern. The nonprofit provides soccer training opportunities to youth soccer players looking to improve their game while also affecting the lives of the less fortunate in a positive way. While participating in the training programs the players also go out and raise money for selected charities. The organization then donates the funds. In its first 18 months we donated $10,500. We would like to see designs attempt to symbolize the mission of the nonprofit - essentially "improve you while improving someone else."

We would like to see the following features:

· A place to donate - Our intent is to have the home page linked to the donation page; a simple straight-forward process for people to give money, and make donating as painless as possible - no account needed to make a donation, credit card or e-check should be the only information needed to donate, and have it be on a single page.

· A photo gallery so people can browse the photo gallery to get a better understanding of our organization and a place to add videos and a calendar to show upcoming events

· A place for contact information and the profiles of directors and board members. This should include a spot showing all the charities the organization donates to. Also includes a news section/blog for comments and suggestions.

We want the design to revolve around the content and mission. We would really like to stress our organization as nonprofit. We would also like if the website was user friendly and easy to navigate.

The logo of our organization is uploaded

```html
<!DOCTYPE html>
<html lang="en">
<head>
<meta charset="utf-8">
<title>Lend a Lantern</title>
<link href="https://fonts.googleapis.com/css2?family=Kalam:wght@400;700&family=Open+Sans:wght@400;600;700&display=swap" rel="stylesheet">
<style>
:root{
  --green:#5b8c3a;
  --green-dark:#3e5e2a;
  --green-deep:#2f4a20;
  --green-light:#a9c86e;
  --green-pale:#e8f0da;
  --orange:#f26a21;
  --ink:#333;
  --muted:#666;
  --white:#fff;
  --line:#cfd8c4;
}
*{box-sizing:border-box;margin:0;padding:0}
html,body{width:822px;height:1200px;overflow:hidden}
body{font-family:"Open Sans",Arial,sans-serif;color:var(--ink);background:#fff;position:relative;font-size:11px}
.page{position:relative;width:822px;height:1200px;background:#f4f6f0}

/* header */
.site-header{position:absolute;left:0;top:0;width:822px;height:140px;background:#fff}
.brand{position:absolute;left:24px;top:18px;width:150px}
.brand-mark{display:block;width:28px;height:28px;background:var(--green);margin-bottom:6px}
.brand-name{display:block;font-family:"Open Sans",sans-serif;font-weight:700;font-size:21px;color:var(--green);line-height:1.05}
.tagline{position:absolute;left:200px;top:30px;width:590px;font-family:"Kalam",cursive;font-size:29px;line-height:1.2;color:var(--green-dark);white-space:nowrap}
.search{position:absolute;right:22px;top:10px;width:120px;height:20px;border:1px solid #bbb;font-size:9px;color:#999;padding:3px 6px;display:flex;justify-content:space-between}

/* nav */
.main-nav{position:absolute;left:0;top:140px;width:822px;height:32px;background:var(--green);display:flex;align-items:center;padding-left:22px}
.main-nav a{color:#fff;text-decoration:none;font-size:15px;padding:0 20px;height:32px;line-height:32px}
.main-nav .active{background:var(--green-dark)}
.main-nav .donate{background:var(--orange);margin-left:10px}
.dropdown{position:absolute;left:242px;top:172px;width:70px;background:var(--green-dark);z-index:5}
.dropdown a{display:block;color:#fff;font-size:13px;padding:6px 10px;border-bottom:1px solid var(--green)}

/* hero */
.hero{position:absolute;left:22px;top:172px;width:505px;height:280px;background:linear-gradient(160deg,#9bb4c9,#6d8a4a 60%,#a33b36);}
.hero-caption{position:absolute;left:0;bottom:0;width:100%;height:30px;background:rgba(40,60,25,.7);color:#fff;font-size:15px;padding:5px 12px}
.hero-dots{position:absolute;right:14px;bottom:10px;display:flex;gap:5px}
.hero-dots span{width:8px;height:8px;border-radius:50%;background:#fff;opacity:.6}
.hero-dots span:first-child{opacity:1}
.hero-arrow{position:absolute;top:120px;width:20px;height:32px;background:rgba(0,0,0,.35)}
.hero-arrow.prev{left:0}.hero-arrow.next{right:0}

/* donation */
.donation{position:absolute;left:532px;top:172px;width:268px;height:290px;background:var(--green-dark);color:#fff;padding:0 10px}
.donation h2{font-weight:400;font-size:20px;text-align:center;margin:0 -10px;background:var(--green);padding:3px 0}
.field-label{font-size:13px;margin-top:6px}
.select{width:60px;height:20px;background:#fff;color:#333;font-size:11px;padding:2px 5px;display:inline-block;border:1px solid #999}
.input{height:20px;background:#fff;border:1px solid #999;display:inline-block;vertical-align:middle}
.cards{display:flex;gap:5px;margin-top:4px}
.cards span{width:30px;height:18px;background:#fff;border-radius:2px}
.details{border:1px solid var(--green-light);padding:4px 8px 8px;margin-top:8px}
.details legend{font-size:12px;padding:0 4px}
.submit{display:block;text-align:center;color:#fff;font-size:18px;border-top:1px solid var(--green-light);border-bottom:1px solid var(--green-light);margin-top:10px;padding:2px 0}

/* news */
.news{position:absolute;left:22px;top:458px;width:505px;height:272px;background:#fff;border:1px solid var(--line)}
.tabs{display:flex;border-bottom:2px solid var(--green)}
.tabs span{font-size:14px;padding:4px 20px;border:1px solid var(--line);border-bottom:none}
.tabs .on{background:var(--green-pale);color:var(--green-dark)}
.news-grid{display:grid;grid-template-columns:1fr 1fr;gap:10px 24px;padding:8px 14px}
.news-item h3{font-size:12px;font-weight:400;color:var(--green-dark)}
.news-item p{font-size:9px;color:var(--muted);line-height:1.35}
.more{position:absolute;right:10px;bottom:6px;font-size:10px}

/* events */
.events{position:absolute;left:540px;top:468px;width:260px;height:250px;background:#fff;border:1px solid var(--line)}
.events h2{font-size:15px;font-weight:400;text-align:center;padding:4px;border-bottom:1px solid var(--line)}
.event{padding:4px 8px;border-bottom:1px solid #eee;font-size:9.5px}
.event b{display:block;font-weight:400;color:var(--green-dark)}

/* about band */
.about{position:absolute;left:22px;top:738px;width:778px;height:186px;background:var(--green-light);padding:14px 170px 14px 18px;color:#fff;font-size:13px;line-height:1.5}
.about .lead{font-size:18px}
.portrait{position:absolute;right:26px;top:10px;width:120px;height:130px;background:linear-gradient(#5c6e7c,#2b3a46)}
.president{position:absolute;right:26px;top:144px;width:120px;text-align:center;font-size:13px;line-height:1.2}
.president b{color:var(--orange);font-weight:600;display:block}
.about-link{position:absolute;left:330px;bottom:6px;font-size:10px;color:var(--green-deep)}

/* charities */
.charities{position:absolute;left:22px;top:932px;width:778px;height:98px;background:#fff}
.charities h2{background:var(--orange);color:#fff;text-align:center;font-size:16px;font-weight:600;padding:3px 0}
.charities h2 .light{color:var(--green-pale)}
.charity-row{display:flex;justify-content:space-around;align-items:center;padding:10px 50px}
.charity-row span{width:56px;height:50px;border-radius:50%;background:var(--green-pale);border:2px solid var(--green-light)}
.c-arrow{position:absolute;top:50px;width:0;height:0;border-top:14px solid transparent;border-bottom:14px solid transparent}
.c-arrow.prev{left:10px;border-right:14px solid var(--green)}
.c-arrow.next{right:10px;border-left:14px solid var(--green)}

/* footer */
.site-footer{position:absolute;left:0;top:1030px;width:822px;height:170px;background:var(--green-dark);color:#fff;padding:14px 40px}
.site-footer h2{font-size:20px;font-weight:400}
.site-footer h3{font-size:14px;font-weight:400;margin-top:8px}
.contact-cols{display:flex;gap:50px;font-size:12px;margin-top:4px;line-height:1.5}
.quick-contact{position:absolute;right:22px;top:-20px;width:270px;height:172px;background:#fff;color:var(--ink);border:1px solid var(--line);padding:6px 14px}
.quick-contact h2{font-size:20px;color:var(--ink);text-align:center}
.qc-row{display:flex;align-items:center;gap:6px;font-size:13px;margin-top:6px}
.qc-row .input{flex:1}
.quick-contact .submit{color:var(--ink);border-color:var(--line);margin-top:8px;font-size:16px}
.copyright{position:absolute;left:0;bottom:0;width:100%;text-align:center;font-size:8px;background:var(--green-deep);padding:3px}
</style>
</head>
<body>
<div class="page">
  <header class="site-header">
    <div class="brand"><span class="brand-mark"></span><span class="brand-name">Lend a<br>Lantern</span></div>
    <p class="tagline">"Improve you while improving someone else."</p>
    <div class="search"><span>SEARCH</span><span>&#9906;</span></div>
  </header>

  <nav class="main-nav">
    <a href="#">Home</a><a href="#">About</a><a href="#" class="active">Media</a><a href="#">Directors &amp; Board Members</a><a href="#" class="donate">Donate</a>
  </nav>
  <div class="dropdown"><a href="#">Photos</a><a href="#">Videos</a></div>

  <section class="hero" role="img" aria-label="Photo of youth soccer players in red jerseys holding a ball">
    <span class="hero-arrow prev"></span><span class="hero-arrow next"></span>
    <div class="hero-caption">Summer Training Program</div>
    <div class="hero-dots"><span></span><span></span><span></span><span></span></div>
  </section>

  <aside class="donation">
    <h2>Donation</h2>
    <div class="field-label">Amount</div>
    <span class="select">USD &#9662;</span> <span class="input" style="width:120px"></span>
    <div class="field-label">Payment Method</div>
    <div class="cards"><span></span><span></span><span></span><span></span></div>
    <fieldset class="details">
      <legend>Details (Optional)</legend>
      <div class="field-label" style="margin-top:0">Name</div>
      <span class="select" style="width:40px">Mr &#9662;</span> <span class="input" style="width:150px"></span>
      <div class="field-label">Email Address</div>
      <span class="input" style="width:100%"></span>
    </fieldset>
    <span class="submit">Submit</span>
  </aside>

  <section class="news">
    <div class="tabs"><span class="on">News</span><span>Videos</span></div>
    <div class="news-grid">
      <article class="news-item"><h3>Lorem ipsum dolor sit</h3><p>Consectetur adipiscing elit. Maecenas sed mauris eget purus tincidunt luctus nec at lorem.</p></article>
      <article class="news-item"><h3>Lorem ipsum dolor sit</h3><p>Consectetur adipiscing elit. Maecenas sed mauris eget purus tincidunt luctus nec at lorem.</p></article>
      <article class="news-item"><h3>Lorem ipsum dolor sit</h3><p>Consectetur adipiscing elit. Maecenas sed mauris eget purus tincidunt luctus nec at lorem.</p></article>
      <article class="news-item"><h3>Lorem ipsum dolor sit</h3><p>Consectetur adipiscing elit. Maecenas sed mauris eget purus tincidunt luctus nec at lorem.</p></article>
      <article class="news-item"><h3>Lorem ipsum dolor sit</h3><p>Consectetur adipiscing elit. Maecenas sed mauris eget purus tincidunt luctus nec at lorem.</p></article>
    </div>
    <span class="more">More News &raquo;</span>
  </section>

  <aside class="events">
    <h2>Upcoming Events</h2>
    <div class="event">Aug 2014<b>Vehicula libero sagittis tacit sociosqu</b></div>
    <div class="event">Aug 2014<b>Vehicula libero sagittis tacit sociosqu</b></div>
    <div class="event">Aug 2014<b>Vehicula libero sagittis tacit sociosqu</b></div>
    <div class="event">Aug 2014<b>Vehicula libero sagittis tacit sociosqu</b></div>
    <div class="event">Aug 2014<b>Vehicula libero sagittis</b></div>
  </aside>

  <section class="about">
    <p><span class="lead">We</span> are a nonprofit organization based in Des Moines, Iowa. We provides soccer training opportunities to youth soccer players looking to improve their game while also affecting the lives of the less fortunate in a positive way. While participating in the training programs the players also go out and raise money for selected charities. The organization then donates the funds. In its first 18 months we donated $10,500.</p>
    <div class="portrait" role="img" aria-label="Portrait of the organization's president"></div>
    <div class="president"><b>Daniel Reyes</b>President</div>
    <span class="about-link">View Directors and Board Members</span>
  </section>

  <section class="charities">
    <h2>Charities <span class="light">Lend a Lantern</span> Donates To</h2>
    <div class="charity-row"><span></span><span></span><span></span><span></span><span></span></div>
    <span class="c-arrow prev"></span><span class="c-arrow next"></span>
  </section>

  <footer class="site-footer">
    <h2>Contact Us</h2>
    <h3>Office Address</h3>
    <div class="contact-cols">
      <p>Morbi viverra mauris,<br>Vitae pulvinar,<br>Tempus Mauris blandit mi</p>
      <p>Tel 123456789<br><br>Email info@lendalantern.org</p>
    </div>
    <form class="quick-contact">
      <h2>Quick Contact</h2>
      <div class="qc-row">Name <span class="input"></span></div>
      <div class="qc-row">Email Address <span class="input"></span></div>
      <div class="qc-row">Message <span class="input"></span></div>
      <span class="submit">Submit</span>
    </form>
    <div class="copyright">&copy; 2014 Lend a Lantern. All rights reserved</div>
  </footer>
</div>
</body>
</html>
```